Career development coaching - school lever to adults, needs a business card

Tandem Lark - An independent Career Advice business that provides 1-2-1 advice,for career development, entrepreneurial support and workshops needs a business card. Our clients of all ages (school leaver to adults looking for a career move) and universities and colleges. We would like the card to be double-sided with a modern, professional look. Looking for something professional yet very creative and original. Want a standard size business card that inspires a second look because it stands out from the rest.

One side of the card to have a design incorporating the logo with Tandem Lark name with the strap line “Helping you find your future” and space for the company website

Other side of the card to the logo/Tandem Lark name and the usual contact information:
Individual Name
Job Title (for example, Director)
Phone number
Email address
Company website address

Facebook, LinkedIn and Twitter links will need to go somewhere (back or front!)

The design will be used for 3 individuals so should be editable so that we can update as needed/as we grow.

Attached is the company logo/colours to be incorporated.

Target Market(s)

1-2-1 advice,for career development, entrepreneurial support and workshops needs a business card. Our clients of all ages (school leaver to adults looking for a career move) and universities and colleges.

Industry/Entity Type

Consulting

Contact Information for Business Card

Individual Name
Phone number
Email address
Company website address

Font styles to use
Sans Serif

Colors
0255a3
3176b5
faa54b
f78f20
85acd3
cfdeed

Requirements
Must have
• use the Tandem Lark Logo in some way - using the colours and the blue/orange palette
• For the logo - hope this makes sense to someone or if they direclty relate to the logo image attached!
• For the Orange:- Pantone 1585 C
• In CMYK : C3 M71 Y100 K0
• For the Blue:- 100% Pantone 7469 C
• In CMYK : C100 M62 Y27 K7
• Please feel free to contact me with any questions for more info
Nice to have
• happy to see any creative designs
Should not have
• Nothing too traditional,

```html
<!DOCTYPE html>
<html lang="en">
<head>
<meta charset="utf-8">
<title>Tandem Lark – Business Card</title>
<link rel="stylesheet" href="https://fonts.googleapis.com/css2?family=Roboto:wght@400;500&display=swap">
<style>
  :root {
    --backdrop: #3a322d;
    --brand-blue: #13628a;
    --ink-blue: #175c84;
    --brand-orange: #ef7633;
    --paper: #ffffff;
    --text-grey: #6b6b6b;
    --rule-grey: #9a9a9a;
  }
  * { margin: 0; padding: 0; box-sizing: border-box; }
  html, body {
    width: 1200px; height: 1000px; overflow: hidden;
    background: var(--backdrop);
    font-family: "Roboto", sans-serif;
  }
  .card {
    position: absolute; left: 287px; width: 626px; height: 358px;
    border-radius: 28px; text-align: center;
  }
  .card--front { top: 140px; background: var(--brand-blue); color: var(--paper); }
  .card--back { top: 531px; background: var(--paper); }

  .brand-dot {
    position: absolute; left: 50%; transform: translateX(-50%);
    border-radius: 50%; background: var(--brand-orange);
  }
  .card--front .brand-dot { top: 90px; width: 64px; height: 64px; }
  .card--back .brand-dot { top: 68px; width: 52px; height: 52px; }

  .brand-name {
    position: absolute; left: 0; right: 0;
    font-weight: 500; font-variant: small-caps; letter-spacing: 2px;
  }
  .card--front .brand-name { top: 198px; font-size: 38px; color: var(--paper); }
  .card--back .brand-name { top: 158px; font-size: 31px; color: var(--ink-blue); }

  .tagline {
    position: absolute; left: 0; right: 0; top: 241px;
    font-size: 16px; letter-spacing: 1.6px;
  }
  .visit {
    position: absolute; left: 0; right: 0; top: 312px; font-size: 15px;
  }

  .person {
    position: absolute; left: 230px; width: 166px; top: 220px;
    padding-bottom: 4px; border-bottom: 1px solid var(--rule-grey);
    font-size: 14px; color: var(--text-grey);
  }
  .person__name { font-size: 17px; font-weight: 500; color: var(--ink-blue); }
  .contact {
    position: absolute; left: 0; right: 0; top: 256px;
    font-size: 15px; color: var(--text-grey); line-height: 20px;
  }
  .contact__label { color: var(--brand-orange); }
  .contact__web-a { color: var(--ink-blue); }
  .contact__web-b { color: var(--brand-orange); }
  .social {
    position: absolute; left: 0; right: 0; top: 309px;
    display: flex; justify-content: center; gap: 7px;
  }
  .social__box {
    width: 14px; height: 14px; border: 1.3px solid var(--text-grey); border-radius: 2px;
  }
</style>
</head>
<body>
  <section class="card card--front">
    <span class="brand-dot"></span>
    <div class="brand-name">Tandem Lark</div>
    <div class="tagline">Helping you find your future!</div>
    <div class="visit">Visit us: www.TandemLark.com</div>
  </section>

  <section class="card card--back">
    <span class="brand-dot"></span>
    <div class="brand-name">Tandem Lark</div>
    <div class="person"><span class="person__name">Maya Ellison</span> | Director</div>
    <div class="contact">
      <div><span class="contact__label">P.</span> 555-0142-7730 &nbsp;|&nbsp; <span class="contact__label">E.</span> info@tandemlark.com</div>
      <div>www.<span class="contact__web-a">tandem</span><span class="contact__web-b">lark</span>.com</div>
    </div>
    <div class="social" aria-label="Social links">
      <span class="social__box"></span>
      <span class="social__box"></span>
      <span class="social__box"></span>
    </div>
  </section>
</body>
</html>
```